Velisto Events Business Card

We need a business cards that stands out to our clients. We are company who targets prestige clients to spend money with us on experiences, so our image needs to be prestige
Target Market(s)
Corporate
Contact Information for Business Card
There will be four different names on the business cards
Dana Morrowby
Director
O: 02 5147 3086
M: 0451 692 038
E: info@velistoevents.example.au
Facebook: @velistoevents
Instagram: velistoevents
www.velistoevents.example.au
Nathaniel Morrowby
Director
O: 02 5147 3086
M: 0467 215 904
Facebook: @velistoevents
Instagram: velistoevents
www.velistoevents.example.au
Teodor Vinkel
Director
O: 02 5147 3086
M: 0478 903 527
Facebook: @velistoevents
Instagram: velistoevents
www.velistoevents.example.au
Mabel Hartung
Director
O: 02 5147 3086
Facebook: @velistoevents
Instagram: velistoevents
www.velistoevents.example.au
Colors
Designer to choose colors to be used in the design.
Look and feel

```html
<!DOCTYPE html>
<html lang="en">
<head>
<meta charset="utf-8">
<title>Velisto Events Business Card</title>
<link rel="stylesheet" href="https://fonts.googleapis.com/css2?family=Cinzel:wght@400;600&family=Lato:wght@400&display=swap">
<style>
  :root {
    --backdrop: #1b1b1d;
    --navy: #221f52;
    --navy-deep: #1c1946;
    --gold: #c9a35a;
    --gold-light: #e3c88a;
    --ink-light: #e6e3ef;
    --social: #8f8ab8;
  }
  * { margin: 0; padding: 0; box-sizing: border-box; }
  html, body { width: 1200px; height: 852px; overflow: hidden; }
  body {
    background: var(--backdrop);
    position: relative;
    font-family: "Lato", sans-serif;
  }
  .card {
    position: absolute;
    width: 540px;
    height: 310px;
    border-radius: 18px;
    background: linear-gradient(160deg, var(--navy) 0%, var(--navy-deep) 100%);
    overflow: hidden;
  }
  .card--front { left: 40px; top: 271px; }
  .card--back { left: 620px; top: 271px; }

  .wordmark {
    position: absolute;
    font-family: "Cinzel", serif;
    font-weight: 600;
    color: var(--gold);
    text-align: center;
    line-height: 1;
  }
  .wordmark__name { display: block; letter-spacing: 0.32em; }
  .wordmark__sub { display: block; letter-spacing: 0.4em; margin-top: 6px; }

  .card--front .wordmark { left: 0; right: 0; top: 112px; }
  .card--front .wordmark__name { font-size: 34px; }
  .card--front .wordmark__sub { font-size: 13px; }

  .social {
    position: absolute;
    left: 0; right: 0; bottom: 42px;
    display: flex;
    justify-content: center;
    gap: 26px;
    font-size: 13px;
    color: var(--ink-light);
  }
  .social__item { display: flex; align-items: center; gap: 7px; }
  .social__dot {
    width: 14px; height: 14px;
    border-radius: 50%;
    background: var(--social);
  }

  .card--back .wordmark { right: 40px; top: 40px; }
  .card--back .wordmark__name { font-size: 22px; }
  .card--back .wordmark__sub { font-size: 9px; margin-top: 5px; }

  .sprig {
    position: absolute;
    left: 496px; top: 110px;
    width: 10px; height: 32px;
    border-radius: 5px;
    background: linear-gradient(180deg, var(--gold-light), var(--gold));
  }
  .rule {
    position: absolute;
    left: 238px; top: 150px;
    width: 268px; height: 1.5px;
    background: linear-gradient(90deg, rgba(201,163,90,0.2), var(--gold-light));
  }
  .website {
    position: absolute;
    right: 40px; top: 162px;
    display: flex; align-items: center; gap: 7px;
    font-size: 12.5px;
    color: var(--ink-light);
    white-space: nowrap;
  }
  .person { position: absolute; left: 30px; top: 140px; }
  .person__name {
    font-family: "Cinzel", serif;
    font-weight: 600;
    font-size: 18px;
    line-height: 22px;
    letter-spacing: 0.06em;
    color: var(--gold);
    white-space: nowrap;
  }
  .person__role { font-size: 13px; color: var(--ink-light); margin-top: 2px; }

  .contacts {
    position: absolute;
    left: 30px; top: 214px;
    list-style: none;
    font-size: 13px;
    color: var(--ink-light);
  }
  .contacts li { display: flex; align-items: center; gap: 10px; margin-bottom: 9px; }
  .icon { width: 13px; height: 13px; flex: none; }
</style>
</head>
<body>

<section class="card card--front" aria-label="Card front">
  <div class="wordmark">
    <span class="wordmark__name">VELISTO</span>
    <span class="wordmark__sub">EVENTS</span>
  </div>
  <div class="social">
    <span class="social__item"><span class="social__dot"></span>@velistoevents</span>
    <span class="social__item"><span class="social__dot"></span>velistoevents</span>
  </div>
</section>

<section class="card card--back" aria-label="Card back">
  <div class="wordmark">
    <span class="wordmark__name">VELISTO</span>
    <span class="wordmark__sub">EVENTS</span>
  </div>

  <div class="sprig" role="img" aria-label="Small gold laurel sprig ornament"></div>
  <div class="rule"></div>

  <div class="person">
    <p class="person__name">DANA MORROWBY</p>
    <p class="person__role">Director</p>
  </div>

  <div class="website">
    <svg class="icon" viewBox="0 0 16 16" aria-hidden="true">
      <circle cx="8" cy="8" r="6.5" fill="none" stroke="#c9a35a" stroke-width="1.4"/>
      <ellipse cx="8" cy="8" rx="2.8" ry="6.5" fill="none" stroke="#c9a35a" stroke-width="1.2"/>
      <line x1="1.5" y1="8" x2="14.5" y2="8" stroke="#c9a35a" stroke-width="1.2"/>
    </svg>
    www.velistoevents.example.au
  </div>

  <ul class="contacts">
    <li>
      <svg class="icon" viewBox="0 0 16 16" aria-hidden="true">
        <rect x="4" y="1" width="8" height="14" rx="1.5" fill="none" stroke="#c9a35a" stroke-width="1.5"/>
        <circle cx="8" cy="12.3" r="0.9" fill="#c9a35a"/>
      </svg>
      0451 692 038
    </li>
    <li>
      <svg class="icon" viewBox="0 0 16 16" aria-hidden="true">
        <rect x="1" y="3.5" width="14" height="9" rx="1" fill="#c9a35a"/>
        <polyline points="1.5,4 8,9 14.5,4" fill="none" stroke="#221f52" stroke-width="1.3"/>
      </svg>
      info@velistoevents.example.au
    </li>
  </ul>
</section>

</body>
</html>
```